Newspaper Ad for company move to new location

we are moving our facility to a new city and want to make the announcement that we are coming and share some info about our company and the types of jobs we are bringing. The attached document has the type of info we are looking to put in the ad. We want the ad to communicate a family culture and appeal to a rural market for recruiting potential employees. We are a Christian based, family owned company so our ad should reflect our conservative values.

Target Market(s)

Working people in Cedar Springs MI and surrounding 20 mile area

Industry/Entity Type

Manufacture

Font styles to use
Serif

Colors
33a6d7
0393ce

Requirements
Must have
• product photos you can get them at www.trellomark.com

```html
<!DOCTYPE html>
<html lang="en">
<head>
<meta charset="utf-8">
<title>Trellomark is coming to Cedar Springs</title>
<link rel="stylesheet" href="https://fonts.googleapis.com/css2?family=Oswald:wght@400;500;700&family=Open+Sans:wght@400;600;700&display=swap">
<style>
  :root {
    --blue-bright: #33a6d7;
    --blue-core: #0393ce;
    --blue-deep: #0a3f73;
    --blue-night: #06284c;
    --navy-box: #0b2c52;
    --headline-blue: #6fd0f5;
    --green-box: #5f9d3c;
    --white: #ffffff;
    --footer-text: #0a6fa8;
  }
  * { margin: 0; padding: 0; box-sizing: border-box; }
  html, body { width: 776px; height: 1200px; overflow: hidden; background: var(--white); }
  .ad {
    position: relative; width: 776px; height: 1200px;
    font-family: "Open Sans", Arial, sans-serif; color: var(--white);
    background: var(--white);
  }
  .masthead {
    position: absolute; top: 0; left: 0; width: 776px; height: 132px;
    background: var(--white); display: flex; align-items: center; justify-content: center;
  }
  .brand {
    display: flex; align-items: center; gap: 12px;
    font-family: "Oswald", Arial, sans-serif; font-weight: 700; font-size: 40px;
    letter-spacing: 1px; color: var(--blue-deep); text-transform: uppercase;
  }
  .brand-square { width: 34px; height: 34px; background: var(--blue-core); }
  .stage {
    position: absolute; top: 132px; left: 0; width: 776px; height: 1010px;
    background: radial-gradient(ellipse at 50% 28%, var(--blue-core) 0%, #0668a8 38%, var(--blue-deep) 72%, var(--blue-night) 100%);
  }
  .intro { position: absolute; top: 48px; left: 0; width: 100%; text-align: center; }
  .intro .lead {
    font-family: "Oswald", Arial, sans-serif; font-weight: 400; font-size: 17px; letter-spacing: 2px;
  }
  .intro .coming {
    font-family: "Oswald", Arial, sans-serif; font-weight: 700; font-size: 44px;
    letter-spacing: 2px; line-height: 1.1;
  }
  .headline {
    position: absolute; top: 160px; left: 0; width: 100%; text-align: center;
    font-family: "Oswald", Arial, sans-serif; font-weight: 700; font-size: 96px;
    line-height: 1.0; letter-spacing: 2px; color: var(--headline-blue); text-transform: uppercase;
  }
  .about {
    position: absolute; top: 370px; left: 70px; width: 636px; text-align: center;
    font-size: 15.5px; line-height: 1.45;
  }
  .about p + p { margin-top: 18px; }
  .photos { position: absolute; top: 592px; left: 16px; width: 744px; height: 176px; display: flex; gap: 8px; }
  .photo { height: 100%; }
  .photo-containers { width: 278px; background: linear-gradient(135deg, #d9e7c8, #b9cf7a 45%, #e8dfb8); }
  .photo-salad { width: 170px; background: radial-gradient(circle at 50% 50%, #8fbf4d, #d75c3c 55%, #e9ecef 80%); }
  .photo-interior { width: 280px; background: linear-gradient(120deg, #3a3f46, #8d939b 50%, #25292e); }
  .details { position: absolute; top: 776px; left: 16px; width: 744px; height: 226px; display: flex; gap: 0; }
  .positions { width: 250px; background: var(--navy-box); padding: 16px 20px; }
  .offer { width: 236px; padding: 16px 20px; }
  .apply {
    width: 258px; background: var(--green-box); padding: 36px 22px;
    text-align: center; font-size: 14px; line-height: 1.5;
  }
  .apply .email { color: #f4e36b; font-weight: 600; }
  .col-title { font-family: "Oswald", Arial, sans-serif; font-weight: 500; font-size: 20px; color: var(--headline-blue); margin-bottom: 8px; }
  .col-list { list-style: none; font-size: 13.5px; line-height: 1.55; }
  .col-list li::before { content: "\2022"; margin-right: 8px; }
  .footer {
    position: absolute; top: 1142px; left: 0; width: 776px; height: 58px;
    display: flex; align-items: center; justify-content: center;
    font-family: "Oswald", Arial, sans-serif; font-weight: 500; font-size: 20px; color: var(--footer-text);
  }
</style>
</head>
<body>
<div class="ad">
  <header class="masthead">
    <div class="brand"><span class="brand-square"></span>Trellomark</div>
  </header>

  <section class="stage">
    <div class="intro">
      <div class="lead">TRELLOMARK IS</div>
      <div class="coming">COMING TO CEDAR SPRINGS</div>
      <div class="lead">AND WE'RE</div>
    </div>

    <h1 class="headline">Bringing 220<br>Jobs with us!</h1>

    <div class="about">
      <p>We are a family owned company opened in 1967 that has outgrown our Grand Rapids facility. We have purchased the building currently housing Harbor Mill Supply. We expect to start moving equipment to the new location in November.</p>
      <p>Our product line includes packaging for a number of industries including: food, cell phone accessories, hardware, sporting goods, automotive, health, beauty and household items. We also produce decorative parts for the interior of automobiles including trim for the dash, doors and center console.</p>
    </div>

    <div class="photos">
      <div class="photo photo-containers" role="img" aria-label="Printed plastic food containers with lids"></div>
      <div class="photo photo-salad" role="img" aria-label="Clear salad container filled with fresh salad"></div>
      <div class="photo photo-interior" role="img" aria-label="Car dashboard and center console interior trim"></div>
    </div>

    <div class="details">
      <div class="positions">
        <div class="col-title">Some positions we hire for</div>
        <ul class="col-list">
          <li>Mold and Die Makers</li>
          <li>Thermoforming Technicians</li>
          <li>Warehouse</li>
          <li>Packers</li>
          <li>Quality</li>
          <li>Plastics Engineers</li>
          <li>Packaging Engineers</li>
          <li>Trimming Inspectors</li>
        </ul>
      </div>
      <div class="offer">
        <div class="col-title">We Offer</div>
        <ul class="col-list">
          <li>Competitive wages</li>
          <li>Benefits</li>
          <li>Paid Vacation</li>
          <li>Paid Personal Time</li>
          <li>401K Plan</li>
        </ul>
      </div>
      <div class="apply">
        To apply for a position,<br>
        send your resume to<br>
        <span class="email">jobs@trellomark.com</span> or<br>
        2215 Lakeview Ave. NW Grand Rapids,<br>
        MI 49534 or stop in to our Lakeview location<br>
        between 8:00 am and 4:30 pm<br>
        to fill out an application.
      </div>
    </div>
  </section>

  <footer class="footer">Tel.: (616) 555-0142 &nbsp;|&nbsp; www.trellomark.com</footer>
</div>
</body>
</html>
```